Quillbrook Builders Business Cards

I want to use the logo and make an unique business card that shows the textured Logo with brick and builings. I want to be able to stand out when I pass out business cards.

```html
<!DOCTYPE html>
<html lang="en">
<head>
<meta charset="utf-8">
<title>Quillbrook Builders Business Cards</title>
<link rel="stylesheet" href="https://fonts.googleapis.com/css2?family=Oswald:wght@500;700&family=Roboto:ital,wght@0,500;0,700;1,400&display=swap">
<style>
  :root {
    --backdrop: #2b2b2d;
    --concrete-light: #a9a8a5;
    --concrete-mid: #8a8986;
    --concrete-dark: #5f5e5c;
    --paper: #ffffff;
    --brick-red: #d8381f;
    --brick-deep: #8f2414;
    --brick-brown: #7a4a3a;
    --ink: #161616;
    --navy: #1d2a4a;
  }
  * { box-sizing: border-box; margin: 0; padding: 0; }
  html, body { width: 1200px; height: 866px; overflow: hidden; }
  body {
    background: var(--backdrop);
    display: flex; flex-direction: column; align-items: center; justify-content: center;
    gap: 32px;
  }
  .card {
    position: relative;
    width: 672px; height: 384px;
    overflow: hidden;
    background: radial-gradient(ellipse at 45% 55%, var(--concrete-light) 0%, var(--concrete-mid) 55%, var(--concrete-dark) 100%);
    box-shadow: 0 10px 24px rgba(0,0,0,.45);
  }
  .card__paper {
    position: absolute; inset: 0;
    background: var(--paper);
    clip-path: polygon(0 0, 100% 0, 100% 70%, 0 18%);
  }
  .logo {
    position: absolute;
    display: flex; flex-direction: column; align-items: center;
  }
  .logo__art {
    border-radius: 6px;
    background: linear-gradient(160deg, var(--brick-brown) 0%, var(--brick-red) 55%, var(--brick-deep) 100%);
  }
  .logo__name {
    margin-top: 8px;
    font-family: "Oswald", sans-serif; font-weight: 700;
    color: var(--brick-red);
    text-transform: uppercase; letter-spacing: 1px;
    white-space: nowrap;
  }
  .card--front .logo { left: 34px; top: 58px; }
  .card--front .logo__art { width: 300px; height: 170px; }
  .card--front .logo__name { font-size: 32px; }

  .contact {
    position: absolute; right: 34px; top: 110px;
    text-align: right;
  }
  .contact__name {
    font-family: "Oswald", sans-serif; font-weight: 700;
    font-size: 34px; color: var(--brick-red);
    text-transform: uppercase; letter-spacing: 1px;
    margin-bottom: 6px;
  }
  .contact__line {
    display: flex; justify-content: flex-end; align-items: center; gap: 8px;
    font-family: "Roboto", sans-serif; font-weight: 700;
    font-size: 15px; color: var(--ink); line-height: 22px;
  }
  .contact__line em { font-style: italic; font-weight: 400; }
  .contact__icon { width: 14px; height: 14px; flex: none; }

  .social {
    position: absolute; right: 34px; bottom: 40px;
    display: flex; gap: 6px;
  }
  .social__tile {
    width: 30px; height: 26px; border-radius: 4px;
    background: var(--brick-red);
  }

  .card--back .logo { left: 50%; top: 44px; transform: translateX(-50%); }
  .card--back .logo__art { width: 340px; height: 200px; }
  .card--back .logo__name { font-size: 34px; }
  .tagline {
    position: absolute; left: 0; right: 0; bottom: 40px;
    text-align: center;
    font-family: "Oswald", sans-serif; font-weight: 500;
    font-size: 20px; color: var(--navy);
  }
</style>
</head>
<body>

<section class="card card--front">
  <div class="card__paper"></div>
  <div class="logo">
    <div class="logo__art" role="img" aria-label="Textured brick city skyline illustration of the company logo"></div>
    <div class="logo__name">Quillbrook Builders</div>
  </div>
  <div class="contact">
    <div class="contact__name">Theo Marlow</div>
    <div class="contact__line"><span>555 014 2087 <em>(Call or Text)</em></span>
      <svg class="contact__icon" viewBox="0 0 24 24"><path fill="var(--brick-red)" d="M6.6 10.8a15 15 0 0 0 6.6 6.6l2.2-2.2c.3-.3.7-.4 1-.2 1.1.4 2.3.6 3.6.6.6 0 1 .4 1 1V20c0 .6-.4 1-1 1A17 17 0 0 1 3 4c0-.6.4-1 1-1h3.5c.6 0 1 .4 1 1 0 1.3.2 2.5.6 3.6.1.3 0 .7-.2 1z"/></svg>
    </div>
    <div class="contact__line"><span>Theo@quillbrookbuilders.com</span>
      <svg class="contact__icon" viewBox="0 0 24 24"><path fill="var(--brick-red)" d="M2 5h20v14H2z"/><path fill="none" stroke="#fff" stroke-width="2" d="M2 5l10 8 10-8"/></svg>
    </div>
    <div class="contact__line"><span>www.quillbrookbuilders.com</span>
      <svg class="contact__icon" viewBox="0 0 24 24"><g fill="none" stroke="var(--brick-red)" stroke-width="2"><circle cx="12" cy="12" r="10"/><ellipse cx="12" cy="12" rx="4" ry="10"/><path d="M2 12h20M4 7h16M4 17h16"/></g></svg>
    </div>
  </div>
  <div class="social" aria-hidden="true">
    <span class="social__tile"></span><span class="social__tile"></span><span class="social__tile"></span><span class="social__tile"></span><span class="social__tile"></span>
  </div>
</section>

<section class="card card--back">
  <div class="logo">
    <div class="logo__art" role="img" aria-label="Textured brick city skyline with mason tools illustration of the company logo"></div>
    <div class="logo__name">Quillbrook Builders</div>
  </div>
  <p class="tagline">Patios - Sidewalks - Retaining Walls - Foundations</p>
</section>

</body>
</html>
```